Moonvale Jewellery Limited - designer pearl and silver jewellery

Designer silver jewellery with a twist that 20% of the net profit will be donated to a charity in India to help abused children

The products are designed to make the wearer not only feel good about how good the jewellery looks but to know they are also helping others less fortunate

All the Jewellery is designed by myself Margaret Doyle and made in 925 Hallmarked sterling silver . The hallmarking is carried out by the Corrick Assay office

This is my first website and will need to be suitable for e-commerce

Target Market(s)

Stylish women with a love of simple and elegant design , not high fashion by timeless simplicity

Number of Pages Required

5+ page

Font styles to use
Sans Serif

Colors
e666a6

Requirements
Must have
• Reference to Sterling silver
• The Pantone ref for my logo background now is white out of 2063
Nice to have
• Fresh and contemporary - Aimed at 25-55 market
• The same consumer would
• Like this product as likes Velmira, Kester Dunne but will also appreciate the fact this product is about helping others as well
• The Jewellery is about clean simple lines , elegance , hand made and styled to be timeless
• The products are designed to be casual and elegant and all feature either natural freshwater pearls or semi precious gemstones
• I also would like a page that customers can arrange to book talks about the design and production of the product . I give these talks generally tomladies groups and explain the manufacturing process and what the charity I’m doing supports

```html
<!DOCTYPE html>
<html lang="en">
<head>
<meta charset="utf-8">
<title>Moonvale Jewellery</title>
<link rel="stylesheet" href="https://fonts.googleapis.com/css2?family=EB+Garamond:wght@400;500;600&display=swap">
<style>
:root{
  --ink:#111111;
  --ink-soft:#2b2b2b;
  --cream:#f9f8e9;
  --paper:#ececec;
  --white:#ffffff;
  --gold:#f2e46e;
  --gold-line:#c9b84a;
  --pink:#e666a6;
  --grey-text:#444444;
  --field-border:#cfc9a6;
}
*{box-sizing:border-box;margin:0;padding:0}
html,body{width:755px;height:1200px;overflow:hidden}
body{position:relative;background:var(--paper);font-family:"EB Garamond",Georgia,serif;color:var(--ink-soft)}
.abs{position:absolute}

/* header */
.site-header{left:0;top:0;width:755px;height:55px;background:var(--ink)}
.brand{left:142px;top:12px;display:flex;align-items:center;gap:6px;color:var(--gold);font-size:17px;font-weight:500;letter-spacing:.3px}
.brand-dot{width:14px;height:14px;border-radius:50%;background:var(--gold)}
.header-rule{left:190px;top:36px;width:424px;height:1px;background:var(--gold-line)}
.header-search{left:340px;top:20px;display:flex}
.header-search .field{width:74px;height:9px;background:var(--white)}
.header-search .btn{width:23px;height:9px;background:#555;color:#eee;font-size:5.5px;text-align:center;line-height:9px}
.account{top:18px;display:flex;align-items:center;gap:5px;color:#ddd;font-size:5.6px}
.main-nav{top:42px;left:340px;display:flex;font-size:6px;color:#eee;letter-spacing:.3px}
.main-nav span{position:relative}
.main-nav .active{color:var(--gold)}
.main-nav .active::before{content:"";position:absolute;left:-4px;right:-4px;top:-6px;height:1px;background:var(--gold)}

/* page panel */
.panel{left:142px;top:75px;width:472px;height:1015px;background:var(--white)}
.hero{left:142px;top:75px;width:472px;height:267px;background:
  radial-gradient(ellipse 38% 55% at 30% 30%,rgba(196,140,100,.85),rgba(196,140,100,0) 70%),
  radial-gradient(ellipse 50% 40% at 25% 80%,rgba(120,110,100,.8),rgba(120,110,100,0) 70%),
  linear-gradient(100deg,#6a4a36 0%,#8a6a54 25%,#6b625a 50%,#45413d 72%,#27231f 100%)}
.hero-title{left:418px;top:143px;width:180px;color:#f4f0e6;font-size:17.5px;line-height:22px;letter-spacing:1.6px;font-weight:400}
.btn-solid{background:var(--gold);color:var(--ink);font-size:7px;letter-spacing:1px;text-align:center;line-height:15px;font-weight:600}
.btn-outline{border-top:1px solid var(--gold);border-bottom:1px solid var(--gold);color:var(--gold);font-size:7px;letter-spacing:1px;text-align:center;line-height:13px}

.cream{background:var(--cream)}
.photo{display:block}
.section-title{font-size:14.5px;color:var(--ink);text-align:center;letter-spacing:.2px;font-weight:400}
.pink-rule{height:2px;background:var(--pink)}
.copy{font-size:5.6px;line-height:9.4px;color:var(--grey-text)}
.copy p+p{margin-top:9px}
.copy strong{color:var(--ink);font-weight:600}
.field{height:11px;background:var(--white);border:1px solid var(--field-border);font-size:5px;color:#999;padding-left:4px;line-height:9px}
.btn-ruled{border-top:1px solid var(--ink);border-bottom:1px solid var(--ink);font-size:7px;letter-spacing:1px;text-align:center;line-height:13px;color:var(--ink);font-weight:600}
.btn-dark{background:#333;color:#f0f0f0;font-size:7px;letter-spacing:1.2px;text-align:center;line-height:15px;font-weight:600}

/* trending */
.trending{left:142px;top:955px;width:472px;height:120px;background:
  radial-gradient(circle at 15% 25%,rgba(255,255,255,.6),rgba(255,255,255,0) 18%),
  radial-gradient(circle at 80% 80%,rgba(255,255,255,.5),rgba(255,255,255,0) 20%),
  linear-gradient(180deg,#d6d6d6,#bcbcbc)}
.trending-title{left:142px;top:963px;width:472px;text-align:center;font-size:12px;letter-spacing:.8px;color:#333;font-weight:400}
.product{top:986px;width:58px;height:58px;border:1px solid #ddd}
.browse{left:345px;top:1052px;width:66px;border-top:1px solid #333;border-bottom:1px solid #333;font-size:6px;text-align:center;line-height:10px;color:#333}

/* footer */
.site-footer{left:0;top:1106px;width:755px;height:94px;background:var(--ink);border-top:1px solid var(--gold-line)}
.social{left:158px;top:1126px;display:flex;gap:17px}
.social span{width:10px;height:10px;border-radius:50%;background:#f0f0f0}
.foot-search{left:158px;top:1150px;display:flex}
.foot-search .field{width:102px;height:10px;border:none}
.foot-search .btn{width:22px;height:10px;background:#555;color:#eee;font-size:5.5px;text-align:center;line-height:10px}
.foot-nav{left:330px;top:1128px;width:96px;text-align:center;color:#f0f0f0;font-size:6px;line-height:9.6px;letter-spacing:.3px;font-weight:600}
.call{left:472px;top:1121px;display:flex;align-items:center;gap:8px;color:#eee;font-size:7px}
.call-icon{width:15px;height:15px;background:var(--gold);display:flex;align-items:center;justify-content:center}
.call-rule{left:472px;top:1142px;width:126px;height:1px;background:#555}
.newsletter{left:472px;top:1154px;font-size:7px;color:#eee;letter-spacing:.3px}
.newsletter b{color:var(--gold);font-weight:500}
.news-form{left:472px;top:1167px;display:flex}
.news-form .field{width:103px;height:10px;border:none;font-size:5px;color:#888}
.news-form .btn{width:23px;height:10px;background:#555;color:#eee;font-size:5.5px;text-align:center;line-height:10px}
.to-top{left:629px;top:1121px;width:12px;height:12px;border:1px solid #8a7f3a}
</style>
</head>
<body>

<header class="site-header abs"></header>
<div class="brand abs"><span class="brand-dot"></span>Moonvale Jewellery</div>
<div class="header-rule abs"></div>
<div class="header-search abs"><div class="field"></div><div class="btn">Search</div></div>
<div class="account abs" style="left:499px">
  <svg width="9" height="10" viewBox="0 0 9 10"><circle cx="4.5" cy="2.6" r="2.4" fill="#ddd"/><path d="M0 10c0-3 2-4.6 4.5-4.6S9 7 9 10z" fill="#ddd"/></svg>join / sign up
</div>
<div class="account abs" style="left:577px">
  <svg width="10" height="10" viewBox="0 0 10 10"><path d="M3 3V2a2 2 0 0 1 4 0v1" stroke="#ddd" fill="none"/><rect x="0.5" y="3" width="9" height="7" fill="#ddd"/></svg>basket: 0
</div>
<nav class="main-nav abs">
  <span style="margin-right:25px">HOME</span>
  <span class="active" style="margin-right:27px">SHOP</span>
  <span style="margin-right:28px">DESIGN &amp; PRODUCTION</span>
  <span style="margin-right:26px">ABOUT</span>
  <span>CONTACT</span>
</nav>

<main>
<div class="panel abs"></div>

<section>
  <div class="hero abs photo" role="img" aria-label="Photograph of hands placing a silver ring among trays of handmade jewellery"></div>
  <h1 class="hero-title abs">Timeless elegance<br>&amp; positive impact</h1>
  <div class="btn-solid abs" style="left:406px;top:237px;width:79px">Shop now</div>
  <div class="btn-outline abs" style="left:506px;top:237px;width:79px">About charity</div>
</section>

<section>
  <div class="cream abs" style="left:142px;top:342px;width:236px;height:187px"></div>
  <h2 class="section-title abs" style="left:142px;top:350px;width:236px">Production Explained</h2>
  <div class="pink-rule abs" style="left:226px;top:374px;width:56px"></div>
  <p class="copy abs" style="left:157px;top:385px;width:208px">You want to discuss design details and production features? Arrange a book to have a conversation with me and get a full explanation about the manufacturing process and charity for Indian children.</p>
  <div class="field abs" style="left:201px;top:427px;width:117px">Full name*</div>
  <div class="field abs" style="left:201px;top:447px;width:117px">Phone number*</div>
  <div class="field abs" style="left:201px;top:467px;width:117px">Email address*</div>
  <div class="btn-ruled abs" style="left:201px;top:486px;width:117px">Book a Talk</div>
  <div class="abs photo" style="left:378px;top:342px;width:236px;height:187px;background:radial-gradient(ellipse 34% 46% at 52% 62%,#b9b6b2 0%,#d2cec8 35%,#ece9e4 65%,#ffffff 100%)" role="img" aria-label="Photograph of a silver heart pendant with pearls on a chain"></div>
</section>

<section>
  <div class="abs photo" style="left:142px;top:529px;width:236px;height:205px;background:linear-gradient(135deg,#ffffff 0%,#c9c3d0 30%,#6f6880 55%,#8e879c 72%,#e9e6ec 100%)" role="img" aria-label="Photograph of a dark freshwater pearl bracelet with a silver clasp"></div>
  <div class="cream abs" style="left:378px;top:529px;width:236px;height:205px"></div>
  <h2 class="section-title abs" style="left:378px;top:554px;width:236px">925 Hallmarked Sterling Silver</h2>
  <div class="pink-rule abs" style="left:461px;top:578px;width:70px"></div>
  <div class="copy abs" style="left:393px;top:588px;width:210px">
    <p>If you're considering buying 925 Sterling Silver, you will no doubt want to know the difference between pure silver and 925 sterling silver. Well, pure silver is not really made up of only silver. It has 99.9% of silver, and a small content composed of other metals such as copper.</p>
    <p>Sterling Silver, on the other hand, consists of 92.5% silver, and the remaining part consists of copper – mostly copper. This is the reason why Sterling Silver is popularly referred to as 925 Sterling Silver or just 925 Silver.</p>
    <p>The reason silver needs to be combined with other metals is that it is very difficult to make great designs with just pure silver, which is very soft and malleable. A bit of hardness has to be introduced, by adding other metals such as copper. That's why jewelers are capable of making the most intricate and complex designs with 925 Sterling Silver.</p>
  </div>
</section>

<section>
  <div class="cream abs" style="left:142px;top:734px;width:236px;height:204px"></div>
  <h2 class="section-title abs" style="left:142px;top:758px;width:236px">Handmade &amp; Styled to be Timeless</h2>
  <div class="pink-rule abs" style="left:226px;top:783px;width:66px"></div>
  <div class="copy abs" style="left:157px;top:793px;width:208px">
    <p>All the Jewellery is designed by myself <strong>Margaret Doyle.</strong></p>
    <p>Handmade products made with freshwater pearls or precious gemstones, making design elegant, simple and timeless.</p>
    <p>20% of the net profit of silver jewellery will be donated to a charity in India to help abused children</p>
  </div>
  <div class="abs photo" style="left:378px;top:734px;width:236px;height:204px;background:linear-gradient(160deg,#ffffff 0%,#f1e6de 35%,#d9cfcb 55%,#aeb1b8 80%,#dfe0e3 100%)" role="img" aria-label="Photograph of a silver ring set with a single pink pearl"></div>
  <div class="btn-dark abs" style="left:338px;top:895px;width:79px">SHOP NOW</div>
</section>

<section>
  <div class="trending abs" role="img" aria-label="Soft silver bokeh background"></div>
  <h2 class="trending-title abs">TRENDING PRODUCTS</h2>
  <svg class="abs" style="left:152px;top:1003px" width="16" height="26" viewBox="0 0 16 26"><path d="M14 1L2 13l12 12" stroke="#8a8a8a" stroke-width="2" fill="none"/></svg>
  <svg class="abs" style="left:586px;top:1003px" width="16" height="26" viewBox="0 0 16 26"><path d="M2 1l12 12L2 25" stroke="#8a8a8a" stroke-width="2" fill="none"/></svg>
  <div class="product abs" style="left:181px;background:linear-gradient(145deg,#f4f3f6,#7d7890 55%,#4c4860)" role="img" aria-label="Pearl stud earrings"></div>
  <div class="product abs" style="left:248px;background:linear-gradient(145deg,#f7f5ee,#e6d79a 55%,#c9c6c0)" role="img" aria-label="Round silver and gold pendant"></div>
  <div class="product abs" style="left:315px;background:linear-gradient(145deg,#f6f6f4,#cfccc6 55%,#a9a7a3)" role="img" aria-label="Silver bar pendant with pearls"></div>
  <div class="product abs" style="left:382px;background:linear-gradient(145deg,#f8f5e2,#ddd4c6 55%,#b9b5ae)" role="img" aria-label="Silver hoop earrings with pearls"></div>
  <div class="product abs" style="left:448px;background:linear-gradient(145deg,#f6f5ef,#e3d49a 55%,#bfbdb8)" role="img" aria-label="Round silver and gold drop earrings"></div>
  <div class="product abs" style="left:515px;background:linear-gradient(145deg,#f7f7f8,#cfd0d5 55%,#9fa1a8)" role="img" aria-label="Silver ring with a grey pearl"></div>
  <div class="browse abs">Browse more</div>
</section>
</main>

<footer class="site-footer abs"></footer>
<div class="social abs" aria-label="Social links"><span></span><span></span><span></span><span></span><span></span></div>
<div class="foot-search abs"><div class="field"></div><div class="btn">Search</div></div>
<nav class="foot-nav abs">HOME<br>SHOP<br>DESIGN &amp; PRODUCTION<br>ABOUT<br>CONTACT</nav>
<div class="call abs">
  <div class="call-icon"><svg width="8" height="10" viewBox="0 0 8 10"><path d="M1 0h2l1 3-1.5 1c.5 1.3 1.2 2.2 2.2 2.7L6 5.5 8 7v2l-1 1C3 10 0 6 0 1z" fill="#111"/></svg></div>
  Call me at +44 (0)20 0000 4172
</div>
<div class="call-rule abs"></div>
<div class="newsletter abs"><b>SIGN UP</b> for the Moonvale newsletter</div>
<div class="news-form abs"><div class="field">Enter your email</div><div class="btn">Send</div></div>
<div class="to-top abs"><svg width="10" height="10" viewBox="0 0 10 10"><path d="M5 8V2M2 5l3-3 3 3" stroke="#8a7f3a" fill="none"/></svg></div>

</body>
</html>
```